Non-profit organisation for street children in Indonesia

Lentera Bocah provides home, education, family and health care for street children and other underprivileged children in Indonesia.

We need an emotional catchy advertisement that will make people aware of the terrible living conditions of street children in Indonesia and the great work the Lentera Bocah Foundation is doing to help these children.

We have 1 photo available for this advertisement. A little girl laying in the streets. This photo can be used with a strong quote such as "Street children whose responsibility?" or "Safer out on streets than at home" or "This child doesn't have the right to have a childhood worth remembering?" or another strong quote. Be creative! It need to touch people!

See some similar advertisements of other non-profit organizations what we very much like:

http://7brightpix.example/wp-content/uploads/2011/07/boldposters41.jpg
http://7brightpix.example/wp-content/uploads/2011/07/affiches-nobles-motifs-058.jpg

Mission
To give every child in the world the opportunity to live a happy and healthy life free of poverty, exploitation, and violence.

Overview
Lentera Bocah Foundation is an independent non-governmental organisation founded in 2005 in the Netherlands and expanded to Indonesia in 2006. Our aim is to improve the lives of children and to protect their rights by providing education, accommodation, family care and medical and legal aid.

Description
Lentera Bocah (Light for Youngsters) Foundation serves homeless and impoverished children by offering them a new path in life. By providing them with the necessary shelter, education, and psychological support directed towards vocational training, mentorship, and micro-credit opportunities, it strives to enable their re-entery into the community as happy and self-sufficient adults.

Facts:
There are 70 million children in Indonesia, nearly 18 million are very poor and estimated 170,000 children live on the streets.

Pitch submissions need to be 960x696 pixels.

Files available 1 photo and logo
Updates

Reason: Dear Designers, We have decided to extend the deadline because we haven't received what we are after. Please make a design in the trend as the following two examples: http://7brightpix.example/wp-content/uploads/2011/07/boldposters41.jpg http://7brightpix.example/wp-content/uploads/2011/07/affiches-nobles-motifs-058.jpg We hope to receive a good design shortly! Thank you Kind regards Lentera Bocah

Target Market(s)

Everybody

Industry/Entity Type

Non-Profit

Requirements
Must have
• 1. A strong quote.
2. Website url: www.lenterabocah.org
3. Mission quote from Lentera Bocah:
Should not have
• To much text.

```html
<!DOCTYPE html>
<html lang="en">
<head>
<meta charset="utf-8">
<title>Lentera Bocah Foundation – Donate Now</title>
<link href="https://fonts.googleapis.com/css2?family=Archivo+Black&family=Arimo:wght@400;700&display=swap" rel="stylesheet">
<style>
  :root {
    --green-dark: #1a6a36;
    --green-light: #1f8a45;
    --white: #ffffff;
    --yellow: #f5e01a;
    --ink: #111111;
    --photo-deep: #140a05;
    --photo-shadow: #2e1608;
    --photo-warm: #8a4514;
    --photo-amber: #d27a22;
    --photo-glow: #e89a3c;
    --photo-pale: #b98a55;
  }
  html, body {
    margin: 0;
    padding: 0;
    width: 1200px;
    height: 870px;
    overflow: hidden;
    background: var(--white);
  }
  .ad {
    position: relative;
    width: 1200px;
    height: 870px;
    overflow: hidden;
    font-family: "Arimo", Arial, sans-serif;
  }
  .header {
    position: absolute;
    left: 0; top: 0;
    width: 1200px; height: 192px;
    background: linear-gradient(180deg, var(--green-dark) 0%, var(--green-light) 100%);
  }
  .brand {
    position: absolute;
    left: 60px; top: 50px;
    display: flex;
    align-items: center;
    gap: 22px;
  }
  .brand-name {
    font-weight: 700;
    color: var(--white);
    font-size: 44px;
    line-height: 44px;
    letter-spacing: 0.5px;
    text-transform: uppercase;
  }
  .brand-name small {
    display: block;
    font-size: 28px;
    line-height: 32px;
    text-transform: none;
  }
  .brand-dot {
    width: 54px; height: 54px;
    border-radius: 50%;
    background: var(--yellow);
  }
  .photo {
    position: absolute;
    left: 0; top: 200px;
    width: 1200px; height: 670px;
    background:
      radial-gradient(ellipse 250px 300px at 960px 470px, var(--photo-glow) 0%, var(--photo-amber) 45%, rgba(210,122,34,0) 100%),
      radial-gradient(ellipse 200px 170px at 730px 90px, var(--photo-amber) 0%, rgba(210,122,34,0.5) 50%, rgba(210,122,34,0) 100%),
      radial-gradient(ellipse 150px 140px at 640px 150px, var(--photo-pale) 0%, rgba(185,138,85,0) 100%),
      radial-gradient(ellipse 160px 130px at 700px 560px, rgba(232,154,60,0.85) 0%, rgba(232,154,60,0) 100%),
      radial-gradient(ellipse 130px 70px at 1080px 130px, var(--photo-shadow) 0%, rgba(46,22,8,0) 100%),
      radial-gradient(ellipse 280px 220px at 430px 560px, rgba(138,69,20,0.7) 0%, rgba(138,69,20,0) 100%),
      radial-gradient(ellipse 260px 170px at 380px 120px, rgba(120,60,20,0.7) 0%, rgba(120,60,20,0) 100%),
      linear-gradient(90deg, var(--photo-deep) 0%, var(--photo-shadow) 30%, var(--photo-warm) 60%, var(--photo-shadow) 100%);
  }
  .quote-band {
    position: absolute;
    left: 0; top: 402px;
    width: 772px; height: 114px;
  }
  .quote-band svg { position: absolute; inset: 0; }
  .quote {
    position: absolute;
    left: 44px; top: 22px;
    margin: 0;
    color: var(--ink);
    font-size: 29px;
    line-height: 38px;
  }
  .quote strong {
    display: block;
    font-size: 32px;
    padding-left: 12px;
  }
  .cta {
    position: absolute;
    left: 58px; top: 560px;
    color: var(--white);
  }
  .cta-title {
    margin: 0;
    font-family: "Archivo Black", "Arial Black", sans-serif;
    font-size: 80px;
    line-height: 80px;
    letter-spacing: -6px;
  }
  .cta-details {
    margin: 14px 0 0;
    font-weight: 700;
    font-size: 18.5px;
    line-height: 28px;
  }
  .cta-url {
    margin: 10px 0 0;
    font-weight: 700;
    font-size: 33px;
    line-height: 40px;
  }
</style>
</head>
<body>
  <main class="ad">
    <header class="header">
      <div class="brand">
        <div class="brand-name"><small>Foundation</small>Lentera<br>Bocah</div>
        <div class="brand-dot"></div>
      </div>
    </header>

    <div class="photo" role="img" aria-label="Warm night photograph of street children: a smiling boy close up on the right making a peace sign, a young girl looking on behind him, other children blurred to the left"></div>

    <div class="quote-band">
      <svg width="772" height="114" viewBox="0 0 772 114" aria-hidden="true">
        <polygon points="0,0 772,0 694,114 0,114" fill="#f5e01a"/>
      </svg>
      <p class="quote">“Our promise to the children we work with...<strong>We will brighten their lives”</strong></p>
    </div>

    <section class="cta">
      <h1 class="cta-title">DONATE NOW!</h1>
      <p class="cta-details">Donate to GIRO 4827 t.a.v. Stichting Lentera Bocah or<br>financial adopt a child on</p>
      <p class="cta-url">www.lenterabocah.org</p>
    </section>
  </main>
</body>
</html>
```